Pitch Deck Design for Startup (Zovo.io)

Graphic Design for Pitch Deck [Pitch Deck content in links below]

Who are we ?

“Zovo” always, never “ZOVO”

Zovo is an platform to easily use & publish algorithms with minimal effort.

Algorithms include:
Artificial Intelligence
Deep Learning
Machine Learning

No matter what type of applications or software users have, they can implement any of our State-of-Art AI algorithms in their apps with 3 lines of code.

Zovo is taming the tangle™

Using Zovo is as easy as just 3 lines of code to be up and running in minutes.

The general idea is that there's a central place for any app to find great algorithms when they want to use AI algorithms/models and implement them with extreme ease and speed, and this place is Zovo.io.

For the information this deck needs to contain, please refer to this google slide: http://lnkq.example/7Rt2kPw, all the information in there are necessary, we need you to transform this deck into a much better looking, clear, colorful, and also stylish & concise deck. If you can give it a bit of Sci-Fi style would be great as well (not a must have)!

You have total freedom to design however you want, just remember three principles:

It needs to establish the brand / image of the Zovo platform to the description above.

Our audience is wide - so use the ‘explain it like I am 5 year-old’ principle.

DO NOT assume specialist knowledge in the audience - make the deck extremely simple, clear, intuitive and compelling!
If there’s something you’re not sure about in the deck, anything, please don’t hesitate to ask us to get it right!!!

In terms of styles, what we like is something fun & modern but doesn’t lose a sense of quality (seriousness).

We want a clear storyline, and the current sequence and the way we organise the info is what we think is good, but it might not be the best way to present in the deck… additional slide ideas can be submitted with in the process.

QUESTIONS? If you have any questions or better suggestions on ANYTHING related to the deck, feel free to let us know at a@zovo.io, we normally respond promptly.

The design of our website uses more than one colors, and it has slight movement when people scrolling as well. Something goes along with its design would be a nice attribute (Note: not a must have, feel free to design your way, if you try to go along with those colors but the deck doesn’t look good, the design would have a very low chance of being selected). Please take a look for your inspirations: http://zovo.io.

Again, any questions, and enquiries, feel free to reach out to us: a@zovo.io

Target Market(s)

Angel Investors (Tech Startups), Developers, Software Companies

Industry/Entity Type

Startup

Font styles to use
Serif

Requirements
Must have
• GOOD DECKS EXAMPLES:
• For your reference, here are some deck designs we like:
• Vantro, NestLoop, Palvermo
• http://lnkq.example/4Hq9ZmD. The reason is: they are simple, clean, right on target, they used very simple but very friendly & nice colors. On every slide, the audience can kinda get the idea at the very first glance.
Nice to have
• If you can use multiple colors (themed in our style) , that would be awesome!
Should not have
• BAD DECKS EXAMPLES:
• The ones we don’t like: http://lnkq.example/8Wn3tbF, http://lnkq.example/5Jc6XrE. The reason? These are very tedious, not intuitive, and the design is very old fashioned. The information design of the deck is not giving great intuitions at the first sight, the audience has to go through all the text to get the idea.

```html
<!DOCTYPE html>
<html lang="en">
<head>
<meta charset="utf-8">
<title>Zovo — Advantages</title>
<link rel="stylesheet" href="https://fonts.googleapis.com/css2?family=Ubuntu:wght@500;700&family=Open+Sans:wght@400&display=swap">
<style>
  :root {
    --board: #555555;
    --paper: #ffffff;
    --teal: #00edcb;
    --violet: #8155e0;
    --ink: #111111;
    --muted: #8c8c8c;
    --white: #ffffff;
  }
  * { margin: 0; padding: 0; box-sizing: border-box; }
  html, body { width: 1200px; height: 1200px; overflow: hidden; }
  body { background: var(--board); position: relative; font-family: "Open Sans", sans-serif; }

  .slide {
    position: absolute; left: 263px; width: 674px;
    background: var(--paper); overflow: hidden;
  }
  .slide--nine { top: 100px; height: 476px; }
  .slide--ten { top: 650px; height: 478px; }

  .ribbon { position: absolute; left: 0; top: 0; width: 250px; height: 140px; }
  .ribbon polygon { fill: var(--teal); }
  .slide-title {
    position: absolute; left: 38px; top: 34px;
    font-family: "Ubuntu", sans-serif; font-weight: 700;
    font-size: 22px; letter-spacing: 0.5px; color: var(--white);
  }

  .brand {
    position: absolute; right: 22px; top: 28px;
    display: flex; align-items: center; gap: 10px;
  }
  .brand-mark { width: 22px; height: 22px; background: var(--violet); border-radius: 3px; }
  .brand-name {
    font-family: "Ubuntu", sans-serif; font-weight: 500;
    font-size: 32px; color: var(--ink); line-height: 1;
  }

  .tile {
    position: absolute; top: 166px; width: 139px; height: 139px;
    background: var(--violet); border-radius: 2px;
    display: flex; flex-direction: column; align-items: center; justify-content: center;
    text-align: center; color: var(--white);
    font-family: "Ubuntu", sans-serif; font-weight: 700;
    font-size: 22px; line-height: 29px; letter-spacing: 0.6px;
  }
  .tile--left { left: 98px; }
  .tile--right { left: 436px; }
  .tile--tight { font-size: 20px; line-height: 26px; letter-spacing: 0.4px; }
  .tile-sub { font-size: 12.5px; line-height: 16px; letter-spacing: 0.5px; }

  .points {
    position: absolute; top: 338px; list-style: none;
    font-size: 12px; line-height: 15.4px; color: var(--muted); letter-spacing: 0.3px;
  }
  .points--left { left: 30px; width: 310px; }
  .points--right { left: 366px; width: 300px; }
  .points li { position: relative; margin-bottom: 8px; }
  .points li::before {
    content: ""; position: absolute; left: -14px; top: 6px;
    width: 5px; height: 5px; border-radius: 50%; background: var(--muted);
  }

  .page-number {
    position: absolute; color: var(--white);
    font-family: "Open Sans", sans-serif; font-size: 44px; line-height: 1;
    transform: translate(-50%, -50%);
  }
  .page-number--nine { left: 1057px; top: 337px; }
  .page-number--ten { left: 1072px; top: 872px; }
</style>
</head>
<body>

<section class="slide slide--nine">
  <svg class="ribbon" viewBox="0 0 250 140" aria-hidden="true">
    <polygon points="0,0 229,0 241,21 63,128 56,126 0,30"/>
  </svg>
  <h2 class="slide-title">Advantages</h2>
  <div class="brand"><span class="brand-mark"></span><span class="brand-name">Zovo</span></div>

  <div class="tile tile--left">FAST<br>EVOLVING</div>
  <div class="tile tile--right">FOCUS<br>ON<br>RESULTS</div>

  <ul class="points points--left">
    <li>Each algorithm are individually managed<br>&amp; handled by focused, specialised creators/teams.</li>
    <li>Models can be improved fast &amp; seamlessly.</li>
  </ul>
  <ul class="points points--right">
    <li>This platform is not helping developers to develop easier, this product is to give them AI algorithmic results instantly.</li>
    <li>Users come to this platform to get/deliver results.</li>
  </ul>
</section>

<section class="slide slide--ten">
  <svg class="ribbon" viewBox="0 0 250 140" aria-hidden="true">
    <polygon points="0,0 229,0 241,21 63,128 56,126 0,30"/>
  </svg>
  <h2 class="slide-title">Advantages</h2>
  <div class="brand"><span class="brand-mark"></span><span class="brand-name">Zovo</span></div>

  <div class="tile tile--left tile--tight">PLATFORM<br>&amp;<br>COMMUNITY</div>
  <div class="tile tile--right">CLOUD<br>&amp; IOT<span class="tile-sub">INTERCHANGEABLE</span></div>

  <ul class="points points--left">
    <li>We know the demands w/ data.</li>
    <li>Our Freemium Model will help us collecting data.</li>
    <li>We help both users &amp; creators to do better by creating w/ more info.</li>
  </ul>
  <ul class="points points--right">
    <li>Extremely easy &amp; high quality model deployment onto IoT devices from the cloud is in the product roadmap.</li>
  </ul>
</section>

<div class="page-number page-number--nine">9</div>
<div class="page-number page-number--ten">10</div>

</body>
</html>
```